Business card design for new software start-up

This design is for a double-sided, colour business card. The requirements are as follows:
PREVIEW IMAGES:
The preview images of the card should be shown on a white background (i.e. no wood veneers etc).
The preview images for the front and back of the card should be presented top to bottom without overlapping.
OVERALL DESIGN:
Clean, crisp and simple
LOGO COLOURS:
Green - CMYK 50C 100Y (PMS 376)
Grey - CMYK 80K
CARD SIZES:
Trim Size (Card Size) 90mm x 55mm
Margin Size: 80mm x 45mm
Bleed Size: 96mm x 61mm (i.e. 3mm bleed)
The corners of the card should be SQUARE and NOT ROUNDED.
CARD ORIENTATION:
Landscape (i.e. horizontal).
FRONT OF CARD:
- White background
- uTrellow logo with tag line
- NodaKite logo scaled to a width of 1.25 inches and not as prominent as the uTrellow logo
- The NodaKite logo should be placed on a plain background, not overlapping any background images
- Details:
Orlando Pitkey
Founder and Chief Software Architect
uTrellow Pty Ltd
Suite 2704, 51-55 Harlow St
Sydney NSW 2000
Australia
M: +61 (0) 555 0142
E: orlando.pitkey@utrellow.example
www.utrellow.example
BACK OF CARD
- uTrellow logo without tag line
- www.utrellow.example
The back of the card should reflect the concept of being ahead of the curve in a simple or abstract way. Some possible ideas are as follows but other creative suggestions will also be considered:
1) A bell curve taking up the entire area, with the uTrellow logo on the right, near a position ahead of the curve;
2) A graphical, curved arrow with the uTrellow logo near the top of the arrow;
3) An abstract curve with the uTrellow logo near the top of the curve.
At least a portion of the background colour should consist of the logo's green colour using colour code CMYK 50C 100Y (PMS 376). For designs that place the logo over a green background, the colour of the dot over the first "i" may be changed so that it is still visible.
SOURCE FILES
Must be in AI format with 2 versions:
(1) With editable texts/fonts to allow for name and address changes in future;
(2) With all text converted to vectors/paths
PRINT FILES
Must be delivered in PDF, TIFF, JPG, EPS and PSD formats
Images should be 300 DPI
Updates
Revision to design for back of card:
The back of the card should also include the web address: www.utrellow.example
At least a portion of the background colour should consist of the logo's green colour. For designs that place the logo over a green background, the colour of the dot over the first "i" may be changed so that it is still visible.
Additional information:
1) The NodaKite logo should be placed on a plain background, not overlapping any background images;
2) The orientation of the card should be landscape (i.e. horizontal).

```html
<!DOCTYPE html>
<html lang="en">
<head>
<meta charset="utf-8">
<title>uTrellow – Business Card</title>
<link rel="stylesheet" href="https://fonts.googleapis.com/css2?family=Open+Sans:wght@400;600;700&family=Arimo:wght@400;700&display=swap">
<style>
  :root {
    --page: #ffffff;
    --name-grey: #58595b;
    --ink: #222222;
    --ink-soft: #3a3a3a;
    --green: #7ac143;
    --card-border: #9a9a9a;
    --badge-top: #1d5aa8;
    --badge-bottom: #0d3f86;
    --back-dark: #4b5a10;
    --back-mid: #8ea816;
    --back-light: #d7ea38;
    --glow: #fbffd0;
  }
  * { margin: 0; padding: 0; box-sizing: border-box; }
  html, body { width: 881px; height: 1200px; overflow: hidden; background: var(--page); }
  body { position: relative; font-family: "Open Sans", sans-serif; color: var(--ink); }

  .card { position: absolute; left: 39px; width: 792px; height: 454px; }
  .card-front { top: 63px; background: #fff; border: 1px solid var(--card-border); box-shadow: 3px 4px 6px rgba(0,0,0,.22); }
  .card-back {
    top: 561px; height: 452px; overflow: hidden;
    background: radial-gradient(ellipse 75% 95% at 78% 55%, var(--back-light) 0%, var(--back-mid) 45%, var(--back-dark) 100%);
    box-shadow: 3px 4px 6px rgba(0,0,0,.25);
  }

  .company-name {
    position: absolute;
    font-family: "Open Sans", sans-serif; font-weight: 400; letter-spacing: 0; line-height: 1;
  }
  .front-name { left: 52px; top: 64px; font-size: 60px; color: var(--name-grey); }

  .tagline {
    position: absolute; left: 436px; top: 64px;
    font-family: "Open Sans", sans-serif; font-weight: 600; font-size: 16px; line-height: 21px;
    color: var(--name-grey); text-transform: uppercase;
  }

  .person-name { position: absolute; left: 54px; top: 172px; font-size: 25px; font-weight: 700; color: var(--ink); }
  .person-title { position: absolute; left: 54px; top: 206px; font-size: 18px; color: var(--ink-soft); }
  .company { position: absolute; left: 54px; top: 243px; font-size: 21px; font-weight: 700; }
  .address { position: absolute; left: 54px; top: 274px; font-size: 18px; line-height: 24px; color: var(--ink-soft); }

  .contact-list { position: absolute; left: 54px; top: 337px; list-style: none; font-size: 18px; line-height: 24px; color: var(--ink-soft); }
  .contact-list li { display: flex; align-items: center; gap: 9px; }
  .contact-icon {
    width: 15px; height: 15px; border-radius: 3px; background: var(--green);
    color: #fff; font-size: 10px; font-weight: 700; display: flex; align-items: center; justify-content: center;
  }

  .partner-badge {
    position: absolute; left: 508px; top: 309px; width: 254px; height: 115px; border-radius: 8px;
    background: linear-gradient(180deg, var(--badge-top), var(--badge-bottom));
  }

  .back-name { left: 49px; top: 66px; font-size: 60px; color: #fff; }

  .bulb-area {
    position: absolute; left: 480px; top: 150px; width: 310px; height: 300px;
    background: radial-gradient(circle at 45% 40%, var(--glow) 0%, rgba(245,255,170,.75) 22%, rgba(215,234,56,0) 62%);
  }

  .back-url {
    position: absolute; left: 49px; top: 398px; font-size: 18px; letter-spacing: 8.5px; color: #fff; font-weight: 400;
  }
  .back-url strong { font-weight: 700; }
</style>
</head>
<body>
  <section class="card card-front" aria-label="Card front">
    <p class="company-name front-name">uTrellow</p>
    <p class="tagline">Software<br>Ahead of<br>The Curve</p>

    <h1 class="person-name">Orlando Pitkey</h1>
    <p class="person-title">Founder &amp; Chief Software Architect</p>

    <h2 class="company">uTrellow Pty Ltd</h2>
    <p class="address">Suite 2704, 51-55 Harlow St<br>Sydney NSW 2000 Australia</p>

    <ul class="contact-list">
      <li><span class="contact-icon">P</span>+61 (0) 555 0142</li>
      <li><span class="contact-icon">E</span>orlando.pitkey@utrellow.example</li>
      <li><span class="contact-icon">W</span>www.utrellow.example</li>
    </ul>

    <div class="partner-badge" role="img" aria-label="NodaKite startup programme badge"></div>
  </section>

  <section class="card card-back" aria-label="Card back">
    <p class="company-name back-name">uTrellow</p>
    <div class="bulb-area" role="img" aria-label="Glowing light bulb illustration"></div>
    <p class="back-url">www.<strong>utrellow</strong>.example</p>
  </section>
</body>
</html>
```